***PLASTIC*** Business Card Design

1 sided business card design
The card will be screen printed on plastic, so colour and fonts must be strong.

Must use the colours in the logo eps attached (Black/Ivory/White). Other colour(s) can be added.

Four (4) examples of how the logo can be printed are included in the logo eps attached.

The business card should highlight the logo. The card will be given to architects, interior designers and builders. It should look sophisticated but also innovative.

Do not cover the whole card with colour as it is important than some of the frosted plastic card is visible.

Be creative.

Target Market(s)

architects, interior designers and builders and wealthy home owners

Industry/Entity Type

Plastic

Requirements
Must have
• Must use the colours in the logo eps attached (Black/Ivory/White). Other colour(s) can be added if necessary.

The font is Square721 ExBT but has been a little thickened. It is not essential that you use this font. The name should be a stronger version of the font than other details.

The card will be printed on PVC - see http://www.vobrelt.com.au/pricelistbcardsplastic.php

Final artwork must be print ready. You must use the printing spec at http://www.vobrelt.com.au/2011%20PVC-TW.pdf

The actual details to be typeset ono the card are:

Rory Pellam

Mobile: 0412 836157
email: info@lumaplastering.com.au
www.lumaplastering.com.au

PO Box 52, Altona, Vic 3018

Plastering | Rendering | Cornicing

```html
<!DOCTYPE html>
<html lang="en">
<head>
<meta charset="utf-8">
<title>Luma Plastering – Business Card</title>
<link href="https://fonts.googleapis.com/css2?family=Questrial&display=swap" rel="stylesheet">
<style>
  :root {
    --page: #ffffff;
    --card: #ffffff;
    --card-edge: #cfcfcf;
    --ink: #000000;
    --reverse: #ffffff;
  }
  html, body {
    margin: 0;
    padding: 0;
    width: 1200px;
    height: 720px;
    overflow: hidden;
    background: var(--page);
  }
  .canvas {
    position: relative;
    width: 1200px;
    height: 720px;
    font-family: "Questrial", "Century Gothic", sans-serif;
    color: var(--ink);
  }
  .card {
    position: absolute;
    left: 343px;
    top: 199px;
    width: 487px;
    height: 291px;
    background: var(--card);
    border: 1px solid var(--card-edge);
    border-radius: 15px;
    overflow: hidden;
    box-sizing: border-box;
  }
  .brand-band {
    position: absolute;
    left: 0;
    top: 24px;
    width: 100%;
    height: 122px;
    background: var(--ink);
    display: flex;
    align-items: center;
    justify-content: center;
  }
  .brand-name {
    margin: 0;
    padding-top: 4px;
    color: var(--reverse);
    font-weight: 400;
    text-transform: uppercase;
    text-align: center;
    line-height: 1;
  }
  .brand-name__main {
    display: block;
    font-size: 46px;
    letter-spacing: 3px;
  }
  .brand-name__sub {
    display: block;
    margin-top: 7px;
    font-size: 17px;
    letter-spacing: 5px;
  }
  .contact {
    position: absolute;
    top: 163px;
    font-size: 15.5px;
    line-height: 21px;
    margin: 0;
  }
  .contact--left { left: 14px; }
  .contact--right { right: 14px; text-align: right; }
  .contact .person,
  .contact .phone { font-size: 17px; }
  .services-band {
    position: absolute;
    left: 0;
    top: 226px;
    width: 100%;
    height: 27px;
    background: var(--ink);
    color: var(--reverse);
    font-size: 13.5px;
    display: flex;
    align-items: center;
    justify-content: center;
    white-space: pre;
  }
  .website {
    position: absolute;
    left: 0;
    top: 261px;
    width: 100%;
    text-align: center;
    font-size: 17px;
  }
</style>
</head>
<body>
<div class="canvas">
  <section class="card">
    <div class="brand-band">
      <p class="brand-name">
        <span class="brand-name__main">Luma</span>
        <span class="brand-name__sub">Plastering</span>
      </p>
    </div>
    <div class="contact contact--left">
      <div class="person">Rory Pellam</div>
      <div class="address">PO Box 52, Kelmont, Vic 3027</div>
    </div>
    <div class="contact contact--right">
      <div class="phone">0412 836157</div>
      <div class="email">info@lumaplastering.com.au</div>
    </div>
    <div class="services-band">Plastering  |  Rendering  |  Cornicing</div>
    <div class="website">www.lumaplastering.com.au</div>
  </section>
</div>
</body>
</html>
```